Business Cards for Financial Service Consulting Business Ltd

Business Card Design for my risk management consultancy to the financial service industry
Responsible Lending, Fair Charges, Ethical Collections

Should be serious, professional, corporate

Target Market(s)

Fintech, Financial Services Industry

Industry/Entity Type

Financial Service

Contact Information for Business Card

Marcus Pennick
marc@larchwellconsulting.co.uk
07700900418
01632960527

Font styles to use
Serif

Colors

Designer to choose colors to be used in the design.

Requirements
Must have
• Name: Larchwell Consulting
• Logo, contact details
• The three pillars of my business Responsible Lending, Fair Charges, Ethical Collections
Nice to have
• Corporate Feel
Should not have
• jokes, pretty pictures, cartoons

```html
<!DOCTYPE html>
<html lang="en">
<head>
<meta charset="utf-8">
<title>Larchwell Consulting – Business Cards</title>
<link href="https://fonts.googleapis.com/css2?family=Jost:wght@400;500;700&display=swap" rel="stylesheet">
<style>
  :root {
    --backdrop: #f2f2f2;
    --card-yellow: #f2ea36;
    --ink: #3b3b3b;
    --paper: #ffffff;
  }
  * { margin: 0; padding: 0; box-sizing: border-box; }
  html, body {
    width: 1200px; height: 864px; overflow: hidden;
    background: var(--backdrop);
    font-family: "Jost", "Futura", sans-serif;
    color: var(--ink);
  }
  .canvas { position: relative; width: 1200px; height: 864px; }

  .card {
    position: absolute;
    width: 520px; height: 300px;
    background: var(--card-yellow);
    overflow: hidden;
    box-shadow: 0 6px 18px rgba(0,0,0,0.12);
  }
  .card--front { left: 50px; top: 282px; }
  .card--back  { left: 630px; top: 282px; }

  /* shared pieces */
  .wordmark {
    position: absolute;
    display: flex; align-items: center; gap: 10px;
    font-weight: 700; color: var(--ink);
    text-transform: uppercase; line-height: 1;
  }
  .wordmark__square { width: 26px; height: 26px; background: var(--ink); flex: none; }
  .wordmark__name { font-size: 24px; letter-spacing: 0.5px; }
  .wordmark__name small { display: block; font-size: 14px; letter-spacing: 1.5px; margin-top: 3px; text-align: right; }

  .corner-tab {
    position: absolute; right: 50px; bottom: 0;
    width: 76px; height: 22px; background: var(--ink);
    clip-path: polygon(14px 0, 100% 0, 100% 100%, 0 100%);
  }

  /* front */
  .holder-rule { position: absolute; left: 0; top: 38px; width: 150px; height: 3px; background: var(--ink); }
  .holder { position: absolute; left: 160px; top: 24px; }
  .holder__name { font-size: 24px; font-weight: 700; line-height: 1; }
  .holder__role { font-size: 15px; font-weight: 400; line-height: 1.2; }

  .contact { position: absolute; left: 22px; top: 78px; font-size: 12px; font-weight: 500; line-height: 15px; }
  .contact__row { display: flex; align-items: flex-start; gap: 10px; margin-bottom: 4px; }
  .contact__icon { width: 20px; height: 20px; flex: none; }

  .stripe-front {
    position: absolute; left: 0; top: 138px; width: 380px; height: 16px; background: var(--ink);
    clip-path: polygon(0 0, 96% 0, 100% 100%, 0 100%);
  }
  .card--front .wordmark { right: 36px; top: 168px; }

  /* back */
  .card--back .wordmark { left: 40px; top: 62px; }
  .pillars {
    position: absolute; left: 0; top: 124px; width: 340px; height: 22px;
    background: var(--ink); color: var(--card-yellow);
    clip-path: polygon(0 0, 96% 0, 100% 100%, 0 100%);
    font-size: 11px; font-weight: 700; line-height: 22px; padding-left: 14px; letter-spacing: 0.3px;
  }
  .back-email { position: absolute; right: 20px; top: 58px; font-size: 12px; font-weight: 500; }
  .back-rule { position: absolute; right: 0; top: 80px; width: 120px; height: 3px; background: var(--ink); }
</style>
</head>
<body>
<main class="canvas">

  <section class="card card--front" aria-label="Business card front">
    <div class="holder-rule"></div>
    <div class="holder">
      <div class="holder__name">Marcus Pennick</div>
      <div class="holder__role">Counselor</div>
    </div>

    <div class="contact">
      <div class="contact__row">
        <svg class="contact__icon" viewBox="0 0 20 20" aria-hidden="true">
          <circle cx="10" cy="10" r="9" fill="none" stroke="#3b3b3b" stroke-width="1.4"/>
          <path d="M7 5.5l1.6 0 .8 2.2-1 .8a6 6 0 0 0 2.6 2.6l.8-1 2.2.8 0 1.6c0 .6-.5 1-1.1 1A7 7 0 0 1 6 6.6c0-.6.4-1.1 1-1.1z" fill="#3b3b3b"/>
        </svg>
        <div>07700900418<br>01632960527</div>
      </div>
      <div class="contact__row">
        <svg class="contact__icon" viewBox="0 0 20 20" aria-hidden="true">
          <circle cx="10" cy="10" r="9" fill="none" stroke="#3b3b3b" stroke-width="1.4"/>
          <rect x="5" y="6.5" width="10" height="7" fill="none" stroke="#3b3b3b" stroke-width="1.2"/>
          <path d="M5 6.5l5 4 5-4" fill="none" stroke="#3b3b3b" stroke-width="1.2"/>
        </svg>
        <div>marc@larchwellconsulting.co.uk</div>
      </div>
    </div>

    <div class="stripe-front"></div>

    <div class="wordmark">
      <span class="wordmark__square"></span>
      <span class="wordmark__name">Larchwell<small>Consulting</small></span>
    </div>

    <div class="corner-tab"></div>
  </section>

  <section class="card card--back" aria-label="Business card back">
    <div class="wordmark">
      <span class="wordmark__square"></span>
      <span class="wordmark__name">Larchwell<small>Consulting</small></span>
    </div>

    <div class="pillars">Lending - Fair Charges - Ethical Collections</div>

    <div class="back-email">marc@larchwellconsulting.co.uk</div>
    <div class="back-rule"></div>

    <div class="corner-tab"></div>
  </section>

</main>
</body>
</html>
```